Korimo Business Cards

Korimo is a software startup and we are looking for business cards that help convey our employee personalities, as well as the professionalism of the company.
Our company font is Comfortaa - and the company logo is attached (we are okay having the text beside the logo if applicable) where we can find the company colour scheme. Cards can be horizontal or vertical format.
We are looking for a two sided business card - on the front we will see the personal details of the employee (name, position, email and phone number), and then on the back, we will see the business details (name and logo, address, phone number, website, email, company tagline: "Accelerating technology disruption in the automotive market")
We want the design to be clean and simple, but also fun, modern, and capturing of a young startup vibe.

```html
<!DOCTYPE html>
<html lang="en">
<head>
<meta charset="utf-8">
<title>Korimo Business Cards</title>
<link rel="stylesheet" href="https://fonts.googleapis.com/css2?family=Comfortaa:wght@400;600;700&display=swap">
<style>
  :root {
    --stage: #e8e8e8;
    --card: #ffffff;
    --ink: #1f1f24;
    --violet: #5a4a9f;
    --magenta: #c2509b;
    --brand: #5d4aa3;
    --band: linear-gradient(90deg, var(--violet), var(--magenta));
  }
  * { margin: 0; padding: 0; box-sizing: border-box; }
  html, body { width: 1200px; height: 413px; overflow: hidden; }
  body {
    background: var(--stage);
    font-family: "Comfortaa", sans-serif;
    color: var(--ink);
    position: relative;
  }
  .card {
    position: absolute;
    top: 82px;
    width: 438px;
    height: 250px;
    background: var(--card);
    overflow: hidden;
  }
  .card--company { left: 126px; }
  .card--personal { left: 637px; }

  .band {
    position: absolute;
    left: 0; right: 0;
    top: 237px;
    height: 7px;
    background: var(--band);
  }
  .card--personal .band {
    background: linear-gradient(90deg, var(--magenta), var(--violet));
  }

  .tagline-dot {
    position: absolute;
    left: 14px; top: 26px;
    width: 12px; height: 12px;
    border-radius: 50%;
    background: linear-gradient(135deg, var(--violet), var(--magenta));
  }
  .tagline {
    position: absolute;
    left: 34px; top: 24px;
    font-size: 11px;
    font-weight: 700;
    line-height: 13px;
  }
  .tagline-rule {
    position: absolute;
    left: 34px; top: 58px;
    width: 196px; height: 2px;
    background: var(--band);
  }

  .brand-name {
    position: absolute;
    font-size: 30px;
    font-weight: 700;
    color: var(--brand);
    letter-spacing: -0.5px;
    line-height: 1;
  }
  .card--company .brand-name { left: 318px; top: 76px; }
  .card--personal .brand-name { left: 44px; top: 130px; }

  .info-block {
    position: absolute;
    font-size: 11px;
    line-height: 14px;
    letter-spacing: 0.3px;
  }
  .info-block::before {
    content: "";
    position: absolute;
    top: 1px; bottom: 1px;
    width: 2px;
    background: var(--violet);
  }
  .contact { left: 30px; top: 188px; padding-left: 0; }
  .contact::before { left: -10px; }
  .address { right: 20px; top: 202px; text-align: right; }
  .address::before { right: -10px; }

  .person { left: 249px; top: 60px; }
  .person::before { left: -10px; }
  .person-name {
    font-size: 23px;
    line-height: 24px;
    color: #7b4ca6;
    letter-spacing: 0.5px;
  }
  .person-role {
    font-size: 12px;
    line-height: 14px;
    letter-spacing: 0.8px;
  }
  .personal-contact {
    left: 249px; top: 148px;
    font-size: 12px;
    line-height: 17px;
    letter-spacing: 0.6px;
  }
  .personal-contact::before { left: -10px; }
</style>
</head>
<body>
  <section class="card card--company">
    <span class="tagline-dot"></span>
    <p class="tagline">Accelerating technology<br>disruption in the automotive market</p>
    <span class="tagline-rule"></span>

    <div class="brand-name">korimo</div>

    <div class="info-block contact">
      044-987 654 321<br>
      hello@korimo-mail.com<br>
      www.korimo-site.com
    </div>
    <div class="info-block address">
      17, Larkspur Lane<br>
      30918, Northland
    </div>

    <div class="band"></div>
  </section>

  <section class="card card--personal">
    <div class="brand-name">korimo</div>

    <div class="info-block person">
      <div class="person-name">ELLA MARSH</div>
      <div class="person-role">DIRECTOR</div>
    </div>

    <div class="info-block personal-contact">
      044-987 654 321<br>
      hello@korimo-mail.com
    </div>

    <div class="band"></div>
  </section>
</body>
</html>
```